Corporate flyer highlighting service offering for PR agency

A corporate flyer is needed for a new service offering that we are doing. The product name is HarborLeap it is a marketing and communications services offering for companies who are getting ready to sell their business. If we are really happy with the designer's work, there will be a great deal more projects. I am looking for a clean design with a few pops of color from my site. https://quillmarsh.partners. I am looking for a good design with data in sections. I am looking for a clean design that feels high-end but not cluttered. Please do not use images of people. Please see the following examples of types of designs I like.
https://www.tackboard.example/pin/839201746530918264/
https://www.tackboard.example/pin/402918375561029847/
https://assets.stockvale.example/corporate-flyer-template-KRTPMB
https://designbrook.example/item/corporate-flyer-template/81046395?s_rank=8
https://assets.stockvale.example/corporate-business-flyer-template-93PX7D

I had to place the project on hold as I choose the wrong type of project and did not get many designs as a result. I am reposting this with an updated brief.

Target Market(s)

Business sellers and brokers

Industry/Entity Type

Marketing for business sellers

Font styles to use
Sans Serif

Requirements
Must have
• Good quality design with content in sections. Clean and high end feeling is a must.
Should not have
• A lot of images of people.

```html
<!DOCTYPE html>
<html lang="en">
<head>
<meta charset="utf-8">
<title>HarborLeap Flyer – Quillmarsh Partners</title>
<link href="https://fonts.googleapis.com/css2?family=Open+Sans:ital,wght@0,400;0,600;0,700;0,800;1,400&display=swap" rel="stylesheet">
<style>
:root{
  --stage:#a7a9ac;
  --navy:#1b2a38;
  --blue:#3a8ad6;
  --sky:#5aa9e8;
  --pale:#dcebf8;
  --green:#8cc43f;
  --orange:#f0702a;
  --ink:#3a3f45;
  --white:#ffffff;
}
*{box-sizing:border-box;margin:0;padding:0}
html,body{width:1200px;height:419px;overflow:hidden;background:var(--stage);font-family:"Open Sans",Arial,sans-serif;color:var(--ink)}
.page{position:absolute;top:53px;width:255px;height:329px;background:var(--white);overflow:hidden;box-shadow:2px 3px 5px rgba(0,0,0,.35)}
.page--cover{left:47px}.page--value{left:331px}.page--services{left:613px}.page--deliver{left:886px}
.abs{position:absolute}
.photo{position:absolute}
.body{font-size:3.2px;line-height:1.45;color:var(--ink)}
.body p{margin-bottom:3px}
.footer{position:absolute;left:0;bottom:0;width:255px;height:8px;background:var(--navy)}
.footer__tab{position:absolute;right:0;bottom:0;height:9px;width:80px;background:var(--blue);clip-path:polygon(8% 0,100% 0,100% 100%,0 100%);color:var(--white);font-size:3.4px;display:flex;align-items:center;justify-content:center;gap:2px}
.footer__tab i{display:inline-block;width:3px;height:3px;border:.5px solid var(--white);border-radius:50%}
.brand{position:absolute;text-align:center;font-weight:600;letter-spacing:.3px}
.brand__name{font-size:9.5px;display:block}
.brand__sub{font-size:3.6px;letter-spacing:1.4px;display:block}
.brand__mark{display:inline-block;width:7px;height:7px;background:var(--green);margin-bottom:3px}
.section-bar{position:absolute;left:8px;height:7px;width:170px;display:flex;align-items:center}
.section-bar__icon{width:10px;height:10px;background:var(--green);clip-path:polygon(25% 0,75% 0,100% 50%,75% 100%,25% 100%,0 50%);flex:none;position:relative;z-index:1}
.section-bar__label{height:6px;flex:1;margin-left:-2px;background:var(--green);clip-path:polygon(0 0,100% 0,96% 100%,0 100%);color:var(--white);font-size:3.5px;font-weight:700;padding-left:6px;display:flex;align-items:center;text-transform:uppercase}
.ticks{list-style:none}
.ticks li{position:relative;padding-left:6px;margin-bottom:1.6px}
.ticks li::before{content:"";position:absolute;left:0;top:.6px;width:3px;height:3px;border-radius:50%;background:var(--green)}
.ticks b{font-weight:700;color:var(--navy)}
.aside-quote{font-style:italic;color:var(--green);font-size:3.4px;line-height:1.45}
</style>
</head>
<body>

<!-- Page 1: cover -->
<section class="page page--cover">
  <div class="photo" role="img" aria-label="Open-plan office interior with desks and chairs, tinted blue" style="left:0;top:0;width:255px;height:175px;background:linear-gradient(160deg,#7fb4e4 0%,#4b86c2 45%,#2c4d72 100%)"></div>
  <svg class="abs" style="left:0;top:0" width="255" height="329" viewBox="0 0 255 329">
    <polygon points="0,0 142,0 142,95 0,95" fill="#3a8ad6" opacity=".55"/>
    <polygon points="142,0 255,0 255,115 175,140 142,95" fill="#1b2a38"/>
    <polygon points="0,95 142,95 175,140 0,150" fill="#3a8ad6" opacity=".7"/>
    <polygon points="0,120 66,145 0,170" fill="#5aa9e8" opacity=".6"/>
    <polygon points="0,145 255,175 255,329 0,329" fill="#ffffff"/>
    <polygon points="0,145 180,190 255,150 255,175 180,200 0,160" fill="#3a8ad6" opacity=".0"/>
    <polygon points="160,175 255,140 255,165 180,188" fill="#3a8ad6"/>
  </svg>
  <div class="brand" style="left:150px;top:18px;width:100px;color:var(--white)">
    <span class="brand__mark"></span>
    <span class="brand__name">QUILLMARSH</span>
    <span class="brand__sub">PARTNERS</span>
  </div>
  <h1 class="abs" style="left:8px;top:28px;font-size:11px;font-weight:700;color:var(--navy)">HARBORLEAP</h1>
  <p class="abs" style="left:8px;top:48px;width:130px;font-size:6px;line-height:1.5;font-weight:700;color:var(--white)">HARBORLEAP PROVIDES EXECUTIVES AND BUSINESS OWNERS WITH CLEAR GUIDANCE TO UNLOCK NON-FINANCIAL VALUE AHEAD OF AN EXIT.</p>
  <h2 class="abs" style="left:8px;top:160px;font-size:8px;font-weight:700;color:var(--navy)">HARBORLEAP</h2>
  <div class="abs body" style="left:8px;top:175px;width:150px">
    <p>A strong communication and marketing strategy can significantly increase the value of your business leading up to an exit. Buyers are looking to mitigate risk and unlock potential value as a catalyst for clear growth potential.</p>
  </div>
  <div class="abs body" style="left:8px;top:196px;width:240px">
    <p>Highlighting your company's success in the marketplace, identifying, and mitigating reputation risks before buyers do, enhancing employee engagement, finding hidden opportunities to boost marketing KPIs and showcasing IP, data, and innovation, can make a significant difference in valuation.</p>
    <p>We design and implement communication and marketing strategies that deliver significant increases in brand awareness, identify reputational risks, and enhance brand perception, helping owners and investors to realize premium values for their companies. We support owners and companies through:</p>
  </div>
  <ul class="abs" style="left:10px;top:238px;list-style:none;font-size:4.2px;color:var(--navy)">
    <li style="display:flex;align-items:center;gap:3px;margin-bottom:3px"><span class="section-bar__icon" style="width:8px;height:8px"></span>COMPANY EXIT PREPARATION</li>
    <li style="display:flex;align-items:center;gap:3px;margin-bottom:3px"><span class="section-bar__icon" style="width:8px;height:8px"></span>M&amp;A</li>
    <li style="display:flex;align-items:center;gap:3px;margin-bottom:3px"><span class="section-bar__icon" style="width:8px;height:8px"></span>IPO</li>
    <li style="display:flex;align-items:center;gap:3px;margin-bottom:3px"><span class="section-bar__icon" style="width:8px;height:8px"></span>SPINOFF/DIVESTITURE</li>
    <li style="display:flex;align-items:center;gap:3px"><span class="section-bar__icon" style="width:8px;height:8px"></span>NEW LEADERSHIP/INVESTOR</li>
  </ul>
  <div class="abs aside-quote" style="left:186px;top:243px;width:60px;border-left:.5px solid #cfd6dc;padding-left:3px">
    <p style="margin-bottom:4px">US institutional investors believe that Investor Relations (IR) accounts for a total variance of 30% in a company's valuation – from a premium of 10% for "superb" IR to a discount of 20% for "poor" IR.</p>
    <p>Brightmere Research Group, "Harnessing IR's Power to Impact a Company's Valuation."</p>
  </div>
  <div class="abs body" style="left:8px;top:299px;width:172px">
    <p>Few sellers would list their home without first inspecting, repairing broken items, and making updates to highlight the positive aspects – increasing appeal to buyers. However, countless business owners leave money on the table during corporate exits due to a lack of preparation.</p>
  </div>
  <div class="footer"></div>
  <div class="footer__tab"><i></i>www.quillmarsh.partners</div>
</section>

<!-- Page 2: value -->
<section class="page page--value">
  <div class="brand" style="left:8px;top:6px;width:88px;color:var(--navy)">
    <span class="brand__mark"></span>
    <span class="brand__name">QUILLMARSH</span>
    <span class="brand__sub">PARTNERS</span>
  </div>
  <div class="photo" role="img" aria-label="Laptop on a desk showing financial charts" style="left:120px;top:17px;width:135px;height:112px;background:linear-gradient(135deg,#c9d8e6 0%,#7fa5c8 50%,#34526f 100%);clip-path:polygon(18% 0,100% 0,100% 100%,0 100%,0 40%)"></div>
  <svg class="abs" style="left:0;top:0" width="255" height="170" viewBox="0 0 255 170">
    <polygon points="0,42 140,42 140,128 0,128" fill="#3a8ad6" opacity=".92"/>
    <polygon points="120,42 160,42 140,128 110,128" fill="#5aa9e8" opacity=".8"/>
    <polygon points="205,128 255,95 255,128" fill="#3a8ad6"/>
    <rect x="0" y="128" width="255" height="34" fill="#1b2a38"/>
  </svg>
  <div class="abs body" style="left:10px;top:64px;width:125px;color:var(--white);font-size:3.5px">
    <p style="margin-bottom:4px">Our team of executive-level communications and marketing experts brings deep buy and sell-side experience. We have played critical roles in the acquisition, integration, and disposition process.</p>
    <p>Our mix of financial services expertise combined with decades of experience leading internal and external communications, marketing and investor relations teams gives us a unique perspective on identifying and unlocking non-financial areas of value and mitigating non-financial risks before exit.</p>
  </div>
  <p class="abs" style="left:10px;top:137px;width:238px;font-size:3.8px;line-height:1.5;font-weight:700;color:var(--white)">While accounting and investment banking teams are hard at work increasing value from a financial perspective, we help organizations enhance their valuation by identifying areas that will appeal most to buyers and ensuring those elements of your business are visible and memorable to those who matter most.</p>
  <h3 class="abs" style="left:10px;top:166px;font-size:4px;font-weight:700;color:var(--navy)">WE HELP COMPANIES INCREASE VALUATION BY:</h3>
  <div class="abs" style="left:10px;top:177px;width:240px;font-size:3.5px;display:grid;grid-template-columns:1fr 1fr;row-gap:5px">
    <div style="display:flex;align-items:center;gap:4px"><span style="width:10px;height:10px;border-radius:50%;background:var(--orange);flex:none"></span>Highlighting value in a clear and visible way</div>
    <div style="display:flex;align-items:center;gap:4px"><span style="width:10px;height:10px;border-radius:50%;background:var(--blue);flex:none"></span>Identifying potential risks and suggesting mitigation measures</div>
    <div style="display:flex;align-items:center;gap:4px"><span style="width:10px;height:10px;border-radius:50%;background:#e8452c;flex:none"></span>Streamlining the exit process</div>
    <div style="display:flex;align-items:center;gap:4px"><span style="width:10px;height:10px;border-radius:50%;background:var(--green);flex:none"></span>Creating a polished presence in the market ahead of buyer interest</div>
  </div>
  <p class="abs" style="left:10px;top:205px;width:238px;font-size:3.6px;line-height:1.45;font-weight:700;color:var(--navy)">HarborLeap provides executives and business owners with clear guidance to unlock value ahead of an exit. Our non-disruptive, ala-carte process enables us to work with sellers on specific areas or to do a complete analysis and recommendation and can include:</p>
  <div class="section-bar" style="top:226px;width:110px"><span class="section-bar__icon"></span><span class="section-bar__label">Brand analysis and recommendations</span></div>
  <div class="abs body" style="left:10px;top:238px;width:240px"><p>Strong brands command a higher valuation. We conduct a brand analysis, providing clear and detailed recommendations to enhance your value proposition and help you stand out from the crowd:</p></div>
  <ul class="abs body ticks" style="left:10px;top:252px;width:165px">
    <li><b>Current external position among competitors</b><br>We look at how your brand measures up based on external competitive analysis, positioning in the media and analyst community, and across other digital channels.</li>
    <li><b>Physical brand image</b><br>A little bit of paint and updated fixtures can go a long way when increasing the value of a home. The same is true for businesses. Our audit evaluates non-disruptive steps your company can take to enhance your brand look and feel before sale.</li>
    <li><b>Employee brand perception</b><br>We conduct a high-level external audit with recommendations to enhance engagement for current and prospective employees.</li>
    <li><b>Customer brand perception</b><br>We conduct a high-level external audit showcasing how customers perceive your brand in the market. We then provide recommendations for enhancing engagement and maximizing value.</li>
  </ul>
  <div class="abs aside-quote" style="left:186px;top:253px;width:62px;font-size:3.1px">
    <p style="margin-bottom:4px">A 5% increase in customer retention correlates with at least a 25% increase in profit, according to an analysis by Corvane &amp; Co. (https://media.corvane.example/retention_costs.pdf)</p>
    <p>It costs 5 times more to acquire a new customer than to retain a current one and 16 times more to get new customers to the same spending level as existing ones. (https://ledgerpine.example/retention-stats/)</p>
  </div>
  <div class="footer"></div>
  <div class="footer__tab"><i></i>www.quillmarsh.partners</div>
</section>

<!-- Page 3: services -->
<section class="page page--services">
  <div class="photo" role="img" aria-label="Business professional touching a digital network of connected icons" style="left:0;top:0;width:255px;height:92px;background:linear-gradient(100deg,#3b4a5c 0%,#7d98b4 40%,#b8cde0 60%,#5c7ea3 100%)"></div>
  <svg class="abs" style="left:0;top:0" width="255" height="100" viewBox="0 0 255 100">
    <polygon points="150,92 255,70 255,92" fill="#3a8ad6"/>
    <polygon points="110,92 200,80 255,92" fill="#5aa9e8" opacity=".8"/>
  </svg>
  <h1 class="abs" style="left:130px;top:27px;font-size:12px;font-weight:700;color:var(--white)">HARBORLEAP</h1>

  <div class="section-bar" style="top:101px;width:170px"><span class="section-bar__icon"></span><span class="section-bar__label">Digital and traditional marketing analysis and recommendations</span></div>
  <div class="abs body" style="left:10px;top:111px;width:238px"><p>How much money are you leaving on the table? Our marketing audits help organizations identify areas of hidden value that can have significant impacts on revenue and valuation. We optimize current activities and uncover new strategies to increase the effectiveness of current marketing spend. Areas we evaluate include:</p></div>
  <ul class="abs body ticks" style="left:10px;top:129px;width:120px">
    <li>Website traffic and conversion</li><li>CRM process review to identify strategies &amp; recommendations</li><li>to increase conversion and reactive old-leads</li><li>Email marketing strategy</li>
  </ul>
  <ul class="abs body ticks" style="left:140px;top:129px;width:110px">
    <li>Automations and drip marketing</li><li>Social media strategy /presence</li><li>Partnership marketing</li><li>Paid media analysis/strategy suggestion</li>
  </ul>

  <div class="section-bar" style="top:163px;width:170px"><span class="section-bar__icon"></span><span class="section-bar__label">Messaging and content strategy review and analysis</span></div>
  <div class="abs body" style="left:10px;top:173px;width:238px"><p>It's about your valuation. Full and fair valuation requires a clear, compelling investment case articulated consistently to the right audience at the right time. Messaging to maximize your value in an acquisition or an IPO is quite different from typical selling messages for prospects, customers, or 'features &amp; business benefits' for press and analysts. We understand the issues and speak the right language to maximize perception of value with key decision makers.</p></div>
  <ul class="abs body ticks" style="left:10px;top:196px;width:238px">
    <li>Review and recommendations of key messaging and value proposition</li>
    <li>Analysis and recommendations to highlight data, IP, and innovation</li>
    <li>Analysis and recommendations to position key executives likely to remain with the company as thought leaders to help build value</li>
    <li>Analysis and recommendations to build employee engagement and retention enhancing your most valuable asset–your team</li>
  </ul>

  <div class="section-bar" style="top:226px;width:170px"><span class="section-bar__icon"></span><span class="section-bar__label">Media and analyst strategy development</span></div>
  <div class="abs body" style="left:10px;top:236px;width:238px"><p>Positive articles and inclusion in analyst reports pack a powerful punch when preparing your business for sale. We work with clients to develop a media strategy that goes beyond brand awareness, leveraging media to build a digital history of third-party validation targeted to enhance appeal to prospective buyers while generating traffic and connections, to enhance overall value.</p></div>
  <ul class="abs body ticks" style="left:10px;top:254px;width:238px">
    <li>Positioning to media and analyst community creating third party market validation</li>
    <li>Key angle recommendations</li>
    <li>Announcement timeline and strategy planning to maximize media value of news</li>
    <li>What is newsworthy</li>
    <li>How to position that news for the most significant impact</li>
  </ul>

  <div class="section-bar" style="top:290px;width:170px"><span class="section-bar__icon"></span><span class="section-bar__label">"White hat/black hat review"</span></div>
  <div class="abs body" style="left:10px;top:301px;width:238px"><p>We take a buyer's communications and marketing approach to analyzing the client company and provide a "punch list" of things a potential buyer is likely to ask/request in due diligence from a comms/culture/marketing/reputation standpoint to ensure that when potential buyers start screening for sellers and evaluating them, the client company has the upper hand.</p></div>
  <div class="footer"></div>
  <div class="footer__tab"><i></i>www.quillmarsh.partners</div>
</section>

<!-- Page 4: deliverables -->
<section class="page page--deliver">
  <div class="photo" role="img" aria-label="Hands using a smartphone beside a laptop with network graphics, blue toned" style="left:0;top:0;width:255px;height:92px;background:linear-gradient(120deg,#1f4466 0%,#3f7fb8 45%,#8fbde6 100%)"></div>
  <svg class="abs" style="left:0;top:0" width="255" height="140" viewBox="0 0 255 140">
    <polygon points="100,92 175,0 255,0 255,92" fill="#3a8ad6" opacity=".85"/>
    <polygon points="175,0 255,0 210,60" fill="#5aa9e8"/>
    <polygon points="235,50 255,20 255,92" fill="#ffffff"/>
    <polygon points="0,92 255,92 255,135 0,135" fill="#1b2a38"/>
    <polygon points="170,92 255,92 230,135 200,135" fill="#3a8ad6"/>
    <polygon points="200,92 255,92 255,135 230,135" fill="#1b2a38"/>
  </svg>
  <p class="abs" style="left:10px;top:104px;width:205px;font-size:3.7px;line-height:1.5;font-weight:600;color:var(--white)">Once the analysis is complete, we deliver actionable intelligence and recommendations to help leaders identify and quickly unlock areas that will boost value and appeal to prospective buyers. Work products include:</p>

  <div class="abs body" style="left:10px;top:146px;width:240px;display:flex;gap:5px">
    <span class="section-bar__icon" style="width:15px;height:15px"></span>
    <div><b style="color:var(--navy)">Gap Assessment</b><br>We provide a comprehensive seller report providing analysis and actionable recommendations to increase your valuation while identifying and mitigating non-financial risks.</div>
  </div>
  <div class="abs body" style="left:10px;top:172px;width:240px;display:flex;gap:5px">
    <span class="section-bar__icon" style="width:15px;height:15px"></span>
    <div><b style="color:var(--navy)">Strategic Roadmap</b><br>Clients are given an actionable tactical roadmap based on the recommendation provided. Organizations can choose to implement key areas or include this powerful guide as part of their presentation to prospective buyers to highlight latent potential. The roadmap provides actionable steps buyers can take upon close as they make their case for your business with their investment committees.</div>
  </div>
  <div class="abs body" style="left:10px;top:207px;width:238px">
    <p style="margin-bottom:6px">Once the strategy integration roadmap is complete, your team can implement it on your timeline, we can work with your team providing guidance and executive-level support, or we can fully execute deliverables with our robust capabilities and team.</p>
    <p style="margin-bottom:6px">Our value proposition, based on delivering outcomes rather than just outputs, means that you receive the benefit and capability of deeply experienced corporate communications leaders without adding headcount or the time to identify, recruit, onboard and retain a new team member.</p>
    <p style="margin-bottom:6px">We help organizations enhance their valuation by identifying areas that will appeal most to buyers and ensuring those elements of your business are visible and memorable to those who matter most.</p>
    <p>HarborLeap helps sellers maximize valuation and unlock hidden potential ahead of an exit–ensuring money is not left on the table.</p>
  </div>
  <p class="abs" style="left:10px;top:273px;width:235px;font-size:4px;line-height:1.4;color:var(--blue)">"Strategy without tactics is the slowest route to victory. Tactics without strategy is the noise before defeat."<br>– Ren Talvo</p>
  <div class="footer"></div>
  <div class="footer__tab"><i></i>www.quillmarsh.partners</div>
</section>

</body>
</html>
```